Landing Page

basically our company has as an strategy to sell our subscription product a set os pages normally in 4 steps
1 - We show that the "customer" will win a prizze
2 - We show some advantages that we have as a company
3 - We show another prizze
4 - We explain that to gain all itens they should make a subscription with a HUGE discount
What do we need?
1 - a new proposal for our set of landing pages
2 - responsive layout for all pages
3 - ideas that can increase our conversion rates
Examples:
http://www.descubravantagens.com/
http://www.descubravantagens.com/vistacam/index.php
http://www.descubravantagens.com/brightdeals/index.php
http://www.descubravantagens.com/v2/index.php
http://atendimentogeral.avaliamos.org.br/index.aspx?prm_id_c=KXR27004
http://www.premiavela.com.br/br_tmk_pro_vsi_int_1.asp?mktcode=TMQW72
https://www.bridgeloop480.info/seq2012/twosteps/pt_br/b2013/index.html?lang=brpt_br&project=TwoSteps&codeprom=FJUB4702&tmpl=b2013&cn=AB11CD22-33EF-4A5B-8C6D-7E8F9A0B1C2D#1
https://atendimentogeral.avaliamos.org.br/step_03.aspx
It Company

```html
<!DOCTYPE html>
<html lang="en">
<head>
<meta charset="utf-8">
<title>Veridano – Customer Prize</title>
<link rel="stylesheet" href="https://fonts.googleapis.com/css2?family=Figtree:wght@400;500;600;700;800&family=Ubuntu:wght@400;500&display=swap">
<style>
:root{
  --green-dark:#0b4d2a;
  --green-a:#c4f02e;
  --green-b:#86c411;
  --blue-a:#2a89cc;
  --blue-b:#0c4a84;
  --blue-box:#1b5f9e;
  --title-blue:#1d68a6;
  --text:#444;
  --muted:#7a7a7a;
  --line:#dedede;
  --red-a:#f04a55;
  --red-b:#d8141f;
  --fb:#2f5b8c;
  --footer:#2e2e2e;
  --gift:#fcb72c;
}
*{box-sizing:border-box;margin:0;padding:0}
html,body{width:1200px;height:999px;overflow:hidden}
body{position:relative;background:#fff;font-family:"Figtree",sans-serif;color:var(--text)}
.abs{position:absolute}

.site-header{position:absolute;left:0;top:0;width:1200px;height:103px;background:#fff}
.brand{left:110px;top:34px;display:flex;align-items:center;gap:10px;font-weight:800;font-size:42px;color:var(--green-dark);letter-spacing:.5px}
.brand-dot{width:14px;height:14px;border-radius:50%;background:var(--green-b)}
.support{right:110px;top:30px;display:flex;align-items:center;gap:8px}
.support-text{text-align:right}
.support-label{font-size:12px;color:#2a3a6a;font-weight:500}
.support-phone{font-size:25px;color:#333;line-height:1}

.hero{position:absolute;left:0;top:103px;width:1200px;height:356px;background:linear-gradient(180deg,var(--blue-a),#1a6aad 55%,var(--blue-b))}
.hero-title{left:110px;top:54px;color:#f2f2f2;text-shadow:0 2px 2px rgba(0,0,0,.25)}
.hero-title .line1{display:block;font-size:39px;font-weight:500;line-height:46px}
.hero-title .line2{display:block;font-size:39px;font-weight:800;line-height:52px}
.hero-copy{left:110px;top:157px;width:560px;font-family:"Ubuntu",sans-serif;font-size:13px;line-height:20px;color:#fff}
.btn-green{display:flex;align-items:center;justify-content:center;background:linear-gradient(180deg,var(--green-a),var(--green-b));border-radius:3px;color:#2d3a10;font-weight:500}
.hero-cta{left:110px;top:234px;width:300px;height:44px;font-size:20px;z-index:2}
.gift{border-radius:6px;background:linear-gradient(135deg,#ffd36a,var(--gift))}

.quote{left:843px;top:62px;width:249px;height:158px;border:1px solid #3a8ad0;border-radius:8px;background:var(--blue-box);color:#fff;font-family:"Ubuntu",sans-serif;font-size:13px;padding:12px 14px}
.quote p{line-height:22px}
.quote .mark{font-family:Georgia,serif;font-size:46px;line-height:20px;vertical-align:-14px;color:#e6eef6;margin-right:6px}
.quote .author{text-align:right;line-height:18px;margin-top:6px}
.quote-tail{left:913px;top:219px}
.thumbs{left:826px;top:264px;display:flex;align-items:center;gap:11px;color:#5aa7e6;font-size:18px}
.thumb{border:2px solid #fff;background:linear-gradient(160deg,#b4876a,#5a4a3e)}
.client-say{left:843px;top:440px;width:249px;height:39px;font-size:20px;color:#1f2a0a}

.tabs{left:110px;top:507px;width:700px;height:48px;display:flex;border:1px solid var(--line);border-radius:3px;background:linear-gradient(#fff,#f1f1f1)}
.tab{display:flex;align-items:center;justify-content:center;font-size:16px;color:#444;border-left:1px solid var(--line)}
.tab.active{background:linear-gradient(180deg,var(--green-a),var(--green-b));border-left:none;color:#2d3a10}
.intro{left:128px;top:583px;width:660px;font-family:"Ubuntu",sans-serif;font-size:13px;line-height:18px;color:var(--muted)}

.benefits{left:110px;top:716px;width:700px;height:131px;border:1px solid var(--line);border-radius:8px;background:linear-gradient(#fff,#f0f0f0)}
.col-line{top:716px;width:1px;height:188px;background:#e8e8e8}
.benefit-title{color:var(--title-blue);font-size:17px;font-weight:600;text-align:center;line-height:20px}
.benefit-note{font-size:12px;line-height:19px;color:#444}
.partner-badge{left:632px;top:689px;width:121px;height:56px;border-radius:4px;background:linear-gradient(#f0505a,var(--red-b))}
.plus{width:42px;height:42px}

.signup{left:833px;top:507px;width:259px;height:397px;border:1px solid #e0e0e0;border-radius:6px;background:linear-gradient(#fff,#e4e4e4);padding:12px 9px}
.signup-lead{font-size:15px;line-height:22px;color:#444}
.btn-social{margin-top:14px;height:43px;border-radius:3px;background:linear-gradient(#4b77a8,var(--fb));display:flex;align-items:center;color:#fff;font-size:19px;font-weight:500;border:1px solid #1f3f66}
.btn-social .sq{width:46px;height:100%;border-right:1px solid #1f3f66;display:flex;align-items:center;justify-content:center}
.btn-social .sq span{width:14px;height:14px;background:#fff}
.btn-social .label{flex:1;text-align:center}
.field-label{display:block;font-size:13px;line-height:16px;color:#666;margin:12px 0 5px}
.field{display:block;width:239px;height:32px;border:1px solid #cfcfcf;border-radius:3px;background:#fff}
.btn-confirm{margin:12px auto 0;width:159px;height:42px;border-radius:3px;background:linear-gradient(var(--red-a),var(--red-b));border:1px solid #a80d16;color:#fff;font-size:20px;display:flex;align-items:center;justify-content:center}

.site-footer{position:absolute;left:0;top:944px;width:1200px;height:55px;background:var(--footer);color:#fff;font-size:13px;display:flex;align-items:center;justify-content:center}
</style>
</head>
<body>

<header class="site-header">
  <div class="abs brand"><span class="brand-dot"></span>VERIDANO</div>
  <div class="abs support">
    <svg width="36" height="36" viewBox="0 0 24 24" aria-hidden="true"><path d="M6.6 10.8a15.1 15.1 0 0 0 6.6 6.6l2.2-2.2c.3-.3.7-.4 1-.2 1.1.4 2.3.6 3.6.6.6 0 1 .4 1 1V20c0 .6-.4 1-1 1A17 17 0 0 1 3 4c0-.6.4-1 1-1h3.5c.6 0 1 .4 1 1 0 1.3.2 2.5.6 3.6.1.3 0 .7-.2 1z" fill="#2b3b5c"/></svg>
    <div class="support-text">
      <div class="support-label">24/7 Online Customer Service</div>
      <div class="support-phone">(11) 4820-1573</div>
    </div>
  </div>
</header>

<section class="hero">
  <h1 class="abs hero-title"><span class="line1">Welcome to a VERIDANO</span><span class="line2">CUSTOMER WILL WIN A PRIZE</span></h1>
  <p class="abs hero-copy">Lorem ipsum dolor sit amet, consectetur adipisicing elit, sed do eiusmod tempor incididunt ut labore et dolore magna aliqua. Ut enim ad minim veniam, quis nostrud exercitation ullamco laboris nisi ut aliquip ex ea commodo consequat.</p>
  <a class="abs btn-green hero-cta">Subcribe Here To Win A Prize</a>

  <div class="abs gift" role="img" aria-label="Small wrapped gift box with orange ribbon" style="left:708px;top:110px;width:68px;height:66px"></div>
  <div class="abs gift" role="img" aria-label="Large wrapped gift box with orange ribbon" style="left:645px;top:226px;width:133px;height:130px"></div>
  <div class="abs gift" role="img" aria-label="Wrapped gift box with orange ribbon, partly out of frame" style="left:0;top:238px;width:98px;height:118px;border-radius:0 6px 0 0"></div>

  <blockquote class="abs quote">
    <p><span class="mark">“</span>Lorem ipsum dolor sit amet, consectetur adipisicing elit, sed do eiusmod tempor incididunt ut labore et dolore magna aliqua...</p>
    <div class="author">Marlon Keats<br>Lorem ipsum dolor sit amet</div>
  </blockquote>
  <svg class="abs quote-tail" width="20" height="18" viewBox="0 0 20 18" aria-hidden="true"><path d="M0 0h20L10 17z" fill="var(--blue-box)" stroke="#3a8ad0"/><path d="M1 0h18" stroke="var(--blue-box)" stroke-width="2"/></svg>

  <div class="abs thumbs">
    <span>‹</span>
    <div class="thumb" role="img" aria-label="Client photo" style="width:51px;height:51px;background:linear-gradient(160deg,#8fbf5a,#7a5a8a)"></div>
    <div class="thumb" role="img" aria-label="Client photo" style="width:61px;height:61px"></div>
    <div class="thumb" role="img" aria-label="Client photo" style="width:51px;height:51px;background:linear-gradient(160deg,#6a3a30,#c98a70)"></div>
    <div class="thumb" role="img" aria-label="Client photo" style="width:51px;height:51px;background:linear-gradient(160deg,#ddd,#666)"></div>
    <span>›</span>
  </div>
</section>
<div class="abs btn-green client-say">What Our Client Say</div>

<nav class="abs tabs">
  <div class="tab active" style="width:129px">Identification</div>
  <div class="tab" style="width:174px">Release of Benefits</div>
  <div class="tab" style="width:209px">Unmissable Opportunity</div>
  <div class="tab" style="width:186px">Additional Advantages</div>
</nav>
<p class="abs intro">Lorem ipsum dolor sit amet, consectetur adipisicing elit, sed do eiusmod tempor incididunt ut labore et dolore magna aliqua. Ut enim ad minim veniam, quis nostrud exercitation ullamco laboris nisi ut aliquip ex ea commodo consequat duis aute irure dolor in reprehenderit in voluptate...</p>

<div class="abs benefits"></div>
<div class="abs col-line" style="left:343px"></div>
<div class="abs col-line" style="left:575px"></div>

<div class="abs" role="img" aria-label="Tablet media player showing a film scene" style="left:158px;top:673px;width:139px;height:89px;border-radius:8px;background:linear-gradient(#3a3a3a,#111);padding:7px"><div style="width:100%;height:100%;background:linear-gradient(90deg,#c9a070,#7a6050)"></div></div>
<div class="abs" role="img" aria-label="Blue gift box with silver ribbon" style="left:413px;top:671px;width:92px;height:91px;background:linear-gradient(135deg,#2b5fd8,#0b2f9a);border-radius:4px"></div>
<div class="abs partner-badge" role="img" aria-label="Partner store badge"></div>

<svg class="abs plus" style="left:322px;top:760px" viewBox="0 0 42 42" aria-hidden="true"><path d="M14 0h14v14h14v14H28v14H14V28H0V14h14z" fill="#cfcfcf"/></svg>
<svg class="abs plus" style="left:554px;top:760px" viewBox="0 0 42 42" aria-hidden="true"><path d="M14 0h14v14h14v14H28v14H14V28H0V14h14z" fill="#cfcfcf"/></svg>

<div class="abs benefit-title" style="left:110px;top:780px;width:233px">A Modern MP5<br>Player with e-reader</div>
<div class="abs benefit-title" style="left:343px;top:780px;width:232px">A Gift incredible<br>surprise!</div>
<div class="abs benefit-title" style="left:575px;top:762px;width:252px">Save up to 30%<br>on exclusive store<br>Shop Swift to<br>Veridano associates!</div>

<p class="abs benefit-note" style="left:128px;top:859px;width:205px">Lorem ipsum dolor sit amet, consectetur adipisicing elit..</p>
<p class="abs benefit-note" style="left:363px;top:859px;width:205px">Lorem ipsum dolor sit amet, consectetur adipisicing elit..</p>
<p class="abs benefit-note" style="left:592px;top:859px;width:205px">Lorem ipsum dolor sit amet, consectetur adipisicing elit..</p>

<form class="abs signup">
  <p class="signup-lead">Login through Linkbook or login below to confirm all these advantages!</p>
  <div class="btn-social"><div class="sq"><span></span></div><div class="label">Login by Linkbook</div></div>
  <label class="field-label">Name:</label><span class="field"></span>
  <label class="field-label">Surname:</label><span class="field"></span>
  <label class="field-label">Email:</label><span class="field"></span>
  <div class="btn-confirm">CONFIRM</div>
</form>

<footer class="site-footer">Copyright 2014.Veridano - All Rights Reserved</footer>
</body>
</html>
```